Business Card Design for new logo

Business card Design for new logo. Follow colors from logo.
The company has offices in multiple comtries
Want to have some bulltes on the countries and also on the main services

Something like
USA*Dominican Republic*LATAM

Consulting*Healthcare IT*Tranformation

Industry/Entity Type

Information Technology

Contact Information for Business Card

Address, Phones, countries, name and position

Lucan morrel

Founder and CEO

947 Tarrow Ln
Marlow bay, PA 17990

Lmorrel@quendoxcare.com

www.quendoxcare.com

555-304-6182

555-222-2222

```html
<!DOCTYPE html>
<html lang="en">
<head>
<meta charset="utf-8">
<title>Quendox Care – Business Card</title>
<link href="https://fonts.googleapis.com/css2?family=Roboto:wght@400;500;700&display=swap" rel="stylesheet">
<style>
  :root {
    --brand-blue: #2573b6;
    --brand-orange: #f58b4f;
    --text-grey: #4a4a4a;
    --rule-grey: #b8b8b8;
    --card-white: #ffffff;
    --canvas-bg: #ecebe8;
  }
  * { margin: 0; padding: 0; box-sizing: border-box; }
  html, body {
    width: 1125px; height: 1200px; overflow: hidden;
    background: var(--canvas-bg);
    font-family: "Roboto", Arial, sans-serif;
  }
  .canvas { position: relative; width: 1125px; height: 1200px; }
  .card {
    position: absolute; left: 165px; width: 800px; height: 457px;
    box-shadow: 0 3px 8px rgba(0,0,0,0.25);
    overflow: hidden;
  }
  .card-front { top: 103px; background: var(--card-white); }
  .card-back { top: 620px; background: var(--brand-orange); }

  .brand-mark {
    position: absolute; right: 37px; top: 152px;
    display: flex; align-items: center; gap: 14px;
  }
  .brand-dot { width: 22px; height: 22px; border-radius: 50%; background: var(--brand-orange); }
  .brand-name { font-size: 44px; font-weight: 500; color: var(--brand-blue); letter-spacing: 0.5px; }

  .name-accent { position: absolute; left: 0; top: 250px; width: 17px; height: 54px; background: var(--brand-blue); }
  .person-name { position: absolute; left: 42px; top: 250px; font-size: 29px; font-weight: 700; color: var(--brand-blue); letter-spacing: 0.3px; }
  .person-title { position: absolute; left: 42px; top: 283px; font-size: 19px; font-weight: 500; color: var(--brand-orange); letter-spacing: 0.3px; }
  .divider { position: absolute; left: 42px; right: 37px; top: 318px; height: 1px; background: var(--rule-grey); }

  .contact-list { position: absolute; left: 44px; top: 337px; list-style: none; }
  .contact-list li { display: flex; align-items: center; height: 25.5px; font-size: 19px; color: var(--text-grey); }
  .contact-icon { width: 18px; height: 18px; margin-right: 11px; fill: var(--brand-blue); }

  .address { position: absolute; right: 36px; top: 348px; text-align: right; font-size: 19px; line-height: 24px; color: var(--text-grey); font-style: normal; }

  .footer-bands { position: absolute; left: 0; top: 404px; width: 800px; height: 53px; }
  .website { position: absolute; right: 36px; top: 419px; font-size: 19px; color: var(--card-white); letter-spacing: 1px; }

  .back-brand {
    position: absolute; left: 0; right: 0; top: 170px;
    display: flex; justify-content: center; align-items: center; gap: 16px;
  }
  .back-brand .brand-dot { width: 30px; height: 30px; background: var(--brand-blue); }
  .back-brand .brand-name { font-size: 58px; color: var(--card-white); }
  .taglines { position: absolute; left: 0; right: 0; top: 366px; text-align: center; font-size: 20px; line-height: 25px; color: var(--card-white); }
</style>
</head>
<body>
<div class="canvas">
  <section class="card card-front">
    <div class="brand-mark">
      <span class="brand-dot"></span>
      <span class="brand-name">Quendox Care</span>
    </div>

    <div class="name-accent"></div>
    <h1 class="person-name">LUCAN MORREL</h1>
    <p class="person-title">FOUNDER &amp; CEO</p>
    <div class="divider"></div>

    <ul class="contact-list">
      <li>
        <svg class="contact-icon" viewBox="0 0 24 24"><path d="M6.6 10.8c1.4 2.8 3.8 5.1 6.6 6.6l2.2-2.2c.3-.3.7-.4 1-.2 1.1.4 2.3.6 3.6.6.6 0 1 .4 1 1V20c0 .6-.4 1-1 1C10.6 21 3 13.4 3 4c0-.6.4-1 1-1h3.5c.6 0 1 .4 1 1 0 1.3.2 2.5.6 3.6.1.3 0 .7-.2 1z"/></svg>
        555-304-6182
      </li>
      <li>
        <svg class="contact-icon" viewBox="0 0 24 24"><path d="M7 1h10c1.1 0 2 .9 2 2v18c0 1.1-.9 2-2 2H7c-1.1 0-2-.9-2-2V3c0-1.1.9-2 2-2zm0 3v14h10V4zm5 15.5a1 1 0 100 2 1 1 0 000-2z"/></svg>
        555-222-2222
      </li>
      <li>
        <svg class="contact-icon" viewBox="0 0 24 24"><path d="M3 6h18v12H3zm1.5 1.5v.4L12 13l7.5-5.1v-.4zm0 2.2v6.8h15V9.7L12 14.8z"/></svg>
        Lmorrel@quendoxcare.com
      </li>
    </ul>

    <address class="address">947 Tarrow Ln<br>Marlow bay, PA 17990</address>

    <svg class="footer-bands" viewBox="0 0 800 53" preserveAspectRatio="none">
      <polygon points="0,14 505,14 490,32 0,32" fill="var(--brand-orange)"/>
      <polygon points="527,0 800,0 800,53 0,53 0,36 492,36" fill="var(--brand-blue)"/>
    </svg>
    <span class="website">www.quendoxcare.com</span>
  </section>

  <section class="card card-back">
    <div class="back-brand">
      <span class="brand-dot"></span>
      <span class="brand-name">Quendox Care</span>
    </div>
    <p class="taglines">USA.Dominican Republic.LATAM<br>Consulting.Healthcare IT.Tranformation</p>
  </section>
</div>
</body>
</html>
```